Wren Pasco Copywriter Website

I am starting a new business as a freelance copywriter. Trying to set up the website for my business is proving to be too technical for me. I would like a simple, clean website using primarily black and white. I have attached the logo I would like used. I would like the menu icons to be Home, Services, Portfolio, Blog, Contact. I would like my mobile phone number (0438 526 914) and email address (wren.pasco.copywriter@mailbrook.example) used in the header of the site. I need the site to be easily manageable and inter-changeable for me to be able to move things around and add images, etc with ease.

I would like the home page to be a static page with space for an image of myself somewhere (I haven't had this taken as yet), an area to put a bit about myself and my business, and also somewhere to include social media icons/links. Again, I would like the whole website and home page to be easily managed so that I can add/delete things with ease.

I would like the image of the typewriter used in the website somewhere also please.

Coding

Number of Pages Required

Font styles to use
Sans Serif
Script

Colors
fdf0f6

Requirements
Must have
• The logo provided
• Ability to change page contents easily
• Ability to add social media icons as needed
Nice to have
• Use of the typewriter image
Should not have
• Complicated pages that are not easily editable

```html
<!DOCTYPE html>
<html lang="en">
<head>
<meta charset="utf-8">
<title>Services – Wren Pasco Copywriter</title>
<link rel="stylesheet" href="https://fonts.googleapis.com/css2?family=Tinos:wght@400;700&family=Catamaran:wght@500&family=Dosis:wght@600;700&display=swap">
<style>
:root{
  --ink:#000;
  --paper:#fff;
  --mist:#f4f4f4;
  --blush:#fdf0f6;
  --line:#555;
  --faint:#f1e3ea;
  --wood-dark:#1c1511;
  --wood-mid:#3e2e22;
}
*{box-sizing:border-box;margin:0;padding:0}
html,body{width:818px;height:1200px;overflow:hidden}
body{position:relative;background:var(--paper);color:var(--ink);font-family:"Tinos",serif}
.abs{position:absolute}
.contact-bar{top:5px;left:0;width:818px;font-size:7.5px;display:flex;justify-content:center;gap:34px}
.hero-typewriter{left:333px;top:75px;width:130px;height:173px;background:linear-gradient(180deg,#ececec 0 22%,#2a2a2a 22% 100%);border-radius:4px}
.brand{left:0;width:818px;top:268px;text-align:center}
.brand-name{display:inline-block;font-family:"Tinos",serif;font-size:15px;padding:2px 22px;background:var(--blush)}
.brand-sub{font-size:5px;letter-spacing:3px;margin-top:1px}
.main-nav{top:375px;left:0;width:818px;display:flex;justify-content:center;gap:22px;font-size:6.4px;font-weight:700;letter-spacing:1.3px}
.main-nav a{color:var(--ink);text-decoration:none}
.content-band{top:390px;left:0;width:818px;height:510px;background:var(--mist)}
.card{background:var(--paper);padding:4px}
.card-inner{border:1px solid var(--line);width:100%;height:100%;position:relative}
.entry{left:154px;top:422px;width:340px;height:453px}
.entry-title{position:absolute;left:26px;top:26px;font-family:"Catamaran",sans-serif;font-weight:500;font-size:15.5px}
.entry-body{position:absolute;left:26px;top:57px;width:282px;font-size:7.1px;line-height:12.35px}
.entry-body p{margin-bottom:12px}
.slider{position:absolute;left:26px;top:252px;width:280px;height:146px;background:linear-gradient(160deg,var(--wood-mid),var(--wood-dark))}
.slider-caption{position:absolute;bottom:0;left:0;width:100%;height:26px;background:rgba(0,0,0,.35);color:var(--paper);text-align:center;font-size:7.5px;padding-top:4px}
.slider-dots{display:flex;justify-content:center;gap:3px;margin-top:2px}
.slider-dots span{width:6px;height:6px;border:1px solid var(--paper);border-radius:50%}
.slider-dots .is-active{background:var(--paper)}
.slider-arrow{position:absolute;top:68px}
.edit-link{position:absolute;left:26px;top:412px;font-size:7px;color:var(--faint)}
.widget{left:511px;width:153px}
.search{top:422px;height:64px}
.search-field{position:absolute;left:17px;top:17px;width:110px;height:21px;border:1px solid var(--line);font-size:5.5px;padding:6px 7px}
.recent{top:507px;height:117px}
.widget-title{font-family:"Dosis",sans-serif;font-weight:700;font-size:7.6px;letter-spacing:1px;text-align:center;border-bottom:1px solid var(--line);height:19px;padding-top:4px}
.recent-list{list-style:none;margin:9px 17px 0}
.recent-list li{font-size:6px;color:var(--faint);height:24px;padding-top:8px;border-bottom:1px solid var(--line)}
.recent-list li:last-child{border-bottom:none}
.gallery{top:646px;height:113px}
.gallery-name{position:absolute;left:0;width:100%;top:43px;text-align:center;font-family:"Dosis",sans-serif;font-weight:700;font-size:13px}
.gallery-arrow{position:absolute;top:42px;width:14px;height:14px;background:#444}
.site-footer{top:900px;left:0;width:818px;height:300px;background:var(--ink);color:var(--paper)}
.footer-heading{position:absolute;top:84px;font-family:"Dosis",sans-serif;font-weight:700;font-size:8px;letter-spacing:1px;text-align:center;width:160px}
.social-row{position:absolute;left:164px;top:106px;display:flex;gap:4px}
.social-row a{width:23.5px;height:23px;background:var(--paper);display:flex;align-items:center;justify-content:center}
.social-row svg{width:11px;height:11px}
.page-list{position:absolute;left:332px;top:104px;width:153px;list-style:none}
.page-list li{height:20px;border-bottom:1px solid var(--paper);text-align:center;font-size:6.5px;font-weight:700;text-decoration:underline;padding-top:5px}
.field{position:absolute;border:1px solid var(--paper);font-size:6px;font-weight:700;padding:7px 7px}
.join-btn{position:absolute;left:616px;top:135px;width:48px;height:21px;border:1px solid var(--paper);font-family:"Dosis",sans-serif;font-weight:700;font-size:6.5px;letter-spacing:1px;text-align:center;padding-top:5px}
.credit{position:absolute;top:247px;left:0;width:818px;text-align:center;font-size:5.6px;font-weight:700}
</style>
</head>
<body>
<header>
  <div class="abs contact-bar"><span>Ph:(+61) 0438 526 914</span><span>Email: wren.pasco.copywriter@mailbrook.example</span></div>
  <div class="abs hero-typewriter" role="img" aria-label="Vintage black typewriter with a blank sheet of paper"></div>
  <div class="abs brand"><div class="brand-name">wren pasco</div><div class="brand-sub">copywriter</div></div>
  <nav class="abs main-nav"><a href="#">HOME</a><a href="#">SERVICES</a><a href="#">PORTFOLIO</a><a href="#">BLOG</a><a href="#">CONTACT</a></nav>
</header>

<div class="abs content-band"></div>

<main class="abs card entry">
  <div class="card-inner">
    <h1 class="entry-title">Services</h1>
    <div class="entry-body">
      <p>Lorem ipsum dolor sit amet, consectetur adipiscing elit. Nullam tincidunt neque at nisl sodales, non dictum tellus porttitor. Nulla sit amet iaculis mi, sed hendrerit mauris. Integer lacus tortor, sollicitudin in eleifend eget, eleifend eu lacus. Fusce pharetra in erat eget sodales. Sed cursus, sem eget elementum commodo, dui diam viverra quam, nec cursus velit ante vel lectus. Sed diam augue, sagittis quis ultricies et, venenatis nec tortor. Nullam vel odio tellus. Phasellus fringilla libero ac massa pulvinar, eu rutrum justo pharetra.</p>
      <p>Fusce nec tellus lectus. Phasellus tincidunt, ante vitae pellentesque condimentum, magna enim consectetur velit, aliquam iaculis quam tellus ac justo. Curabitur ac ipsum vitae dolor euismod facilisis a ultricies sem. Donec vel neque leo. Vivamus eget laoreet turpis. Suspendisse potenti. Praesent lacinia metus nulla, a cursus mauris sagittis vel. Quisque ultricies sed urna in rhoncus. Aenean sed metus id nunc fringilla venenatis. Nunc mauris turpis, aliquet a leo eu, convallis consectetur odio. Morbi gravida, elit a blandit tincidunt, ante erat venenatis nibh, non cursus velit nulla eget ante. Phasellus finibus, turpis a tincidunt pharetra, risus ex bibendum diam, id tristique augue odio vel elit.</p>
    </div>
    <div class="slider" role="img" aria-label="Photo slide: desk from above with typewriter, record, coffee cup and letter tiles">
      <svg class="slider-arrow" style="left:6px" width="12" height="12" viewBox="0 0 12 12"><path d="M7.5 3 4.5 6l3 3" fill="none" stroke="#fff" stroke-width="1.6"/></svg>
      <svg class="slider-arrow" style="right:6px" width="12" height="12" viewBox="0 0 12 12"><path d="M4.5 3 7.5 6l-3 3" fill="none" stroke="#fff" stroke-width="1.6"/></svg>
      <div class="slider-caption">Service 3
        <div class="slider-dots"><span></span><span></span><span class="is-active"></span><span></span><span></span><span></span></div>
      </div>
    </div>
    <span class="edit-link">(Edit)</span>
  </div>
</main>

<aside>
  <section class="abs card widget search"><div class="card-inner"><div class="search-field">Search this website …</div></div></section>
  <section class="abs card widget recent"><div class="card-inner">
    <h2 class="widget-title">RECENT POSTS</h2>
    <ul class="recent-list"><li>Blog Article 3</li><li>Blog Article 2</li><li>Blog Article 1</li></ul>
  </div></section>
  <section class="abs card widget gallery"><div class="card-inner">
    <svg class="gallery-arrow" style="left:26px" viewBox="0 0 14 14"><path d="M8.5 4 5.5 7l3 3" fill="none" stroke="#fff" stroke-width="1.5"/></svg>
    <div class="gallery-name">Snapgrid</div>
    <svg class="gallery-arrow" style="right:26px" viewBox="0 0 14 14"><path d="M5.5 4 8.5 7l-3 3" fill="none" stroke="#fff" stroke-width="1.5"/></svg>
  </div></section>
</aside>

<footer class="abs site-footer">
  <h3 class="footer-heading" style="left:149px">FIND ME</h3>
  <div class="social-row">
    <a href="#" aria-label="Email"><svg viewBox="0 0 12 12"><rect x="1" y="2.5" width="10" height="7" fill="none" stroke="#000" stroke-width="1.2"/><path d="M1 2.5 6 6.5l5-4" fill="none" stroke="#000" stroke-width="1.2"/></svg></a>
    <a href="#" aria-label="Link"><svg viewBox="0 0 12 12"><rect x="0.8" y="4" width="6" height="4" rx="2" fill="none" stroke="#000" stroke-width="1.2"/><rect x="5.2" y="4" width="6" height="4" rx="2" fill="none" stroke="#000" stroke-width="1.2"/></svg></a>
    <a href="#" aria-label="Share"><svg viewBox="0 0 12 12"><path d="M3 6 9 2.5M3 6l6 3.5" stroke="#000" stroke-width="1.1"/><circle cx="3" cy="6" r="1.6"/><circle cx="9" cy="2.5" r="1.6"/><circle cx="9" cy="9.5" r="1.6"/></svg></a>
    <a href="#" aria-label="Website"><svg viewBox="0 0 12 12"><circle cx="6" cy="6" r="4.6" fill="none" stroke="#000" stroke-width="1.1"/><path d="M1.4 6h9.2M6 1.4c-2.4 2.8-2.4 6.4 0 9.2M6 1.4c2.4 2.8 2.4 6.4 0 9.2" fill="none" stroke="#000" stroke-width="0.9"/></svg></a>
    <a href="#" aria-label="Chat"><svg viewBox="0 0 12 12"><path d="M1.5 2h9v6H5L2.5 10.2V8h-1z" fill="none" stroke="#000" stroke-width="1.2" stroke-linejoin="round"/></svg></a>
  </div>
  <h3 class="footer-heading" style="left:329px">PAGES</h3>
  <ul class="page-list"><li>Home</li><li>Portfolio</li><li>Blog</li><li>Contact</li><li>Services</li></ul>
  <h3 class="footer-heading" style="left:507px">JOIN ME</h3>
  <div class="field" style="left:511px;top:106px;width:153px;height:21px">First Name</div>
  <div class="field" style="left:511px;top:135px;width:100px;height:21px">E-Mail Address</div>
  <div class="join-btn">JOIN</div>
  <p class="credit">Handcrafted with <svg width="7" height="6" viewBox="0 0 10 9"><path d="M5 9 .8 4.6A2.5 2.5 0 0 1 5 1.3a2.5 2.5 0 0 1 4.2 3.3z" fill="#fff"/></svg> on the Loomstead Framework</p>
</footer>
</body>
</html>
```